wardrobe/costume stylist needs good business card for own business

Hi:)

I'm wanting a business card for my company. I am a freelance stylist.

I do wardrobe/costume stylist to TV commercials; Films; Fashion and Lifestyle shoots.

I'd like a design based around my name Rosalind Pember written nicely, maybe a colour? Up to you?!

I've attached a couple of images of business cards I like
.... be creative and have fun!

Thank you :)
Updates

Reason: I was trying to get my new business card ready for before I headed overseas Friday morning but I don't think that was realistic so I'd like to extend the deadline to give time to the project. Thank you

Hi designers:) Thank you for all your designs, I've extended the deadline until Sunday, so there's a bit more time. I've attached 3 pictures of business cards which I quite like, please take a look to see if it can be of help in your process. I like the pale plain or patterned background with dark font and the dark plain or patterned background with the pale font the motifs the feminine fonts the plain fonts I like the idea of playing with a circle or some shape on one side of the card with my name or initials as in the picture I have on my post could you play around with this idea a bit please? Thank you all for the work you've done :) Rosa

Hi I am working overseas til Saturday night sorry for no feedback until I teturn Thanks :) Rosa

Hi designers, Thank you all so much for submitting your designs, I really appreciate your input into my project :) I'm sorry I didn't get to respond to some comments, and give feedback. I didn't back from being away until later than I expected, and the deadline had passed then, so apologies. Thanks to you all again for all your really good designs :) Rosa

Target Market(s)

I am a freelance stylist my target audience is producers, production companies, photographers, directors...

Industry/Entity Type

Business

Requirements
Must have
• Rosalind Pember
Stylist or Wardrobe Stylist

email rosapember@quillnet.co.nz
Mobile 0218846193

(Don't have to use the words 'email' and 'mobile')
Nice to have
• Would like it to be double sided
Like B & W
Like pale colour background with dark font or white font
Like dark colour background with pale font
Should not have
• I would prefer it not to incorporate pictures

```html
<!DOCTYPE html>
<html lang="en">
<head>
<meta charset="utf-8">
<title>Rosalind Pember — Stylist business card</title>
<link rel="stylesheet" href="https://fonts.googleapis.com/css2?family=Delius&family=Rye&display=swap">
<style>
  :root {
    --magenta: #e2007a;
    --magenta-soft: #f7c3de;
    --border-pink: #f4b8d6;
    --ink: #1a1a1a;
    --paper: #ffffff;
    --display-font: "Rye", serif;
    --body-font: "Delius", sans-serif;
  }

  * { margin: 0; padding: 0; box-sizing: border-box; }

  html, body {
    width: 1200px;
    height: 420px;
    overflow: hidden;
    background: var(--paper);
  }

  .sheet {
    position: relative;
    width: 1200px;
    height: 420px;
  }

  .card {
    position: absolute;
    top: 48px;
    width: 516px;
    height: 324px;
  }

  /* Front */
  .card--front {
    left: 58px;
    background: var(--paper);
    border: 1.5px solid var(--border-pink);
  }

  .flourish-area {
    position: absolute;
    left: 110px;
    top: 20px;
    width: 330px;
    height: 290px;
    border-radius: 50%;
    background: radial-gradient(ellipse at center, rgba(247, 195, 222, 0.55) 0%, rgba(247, 195, 222, 0.25) 55%, rgba(247, 195, 222, 0) 75%);
  }

  .name-mark {
    position: absolute;
    left: 0;
    top: 0;
    width: 100%;
    font-family: var(--display-font);
    color: var(--magenta);
    font-weight: 400;
    line-height: 1;
  }

  .name-mark__first,
  .name-mark__last {
    position: absolute;
    display: block;
    font-size: 56px;
    white-space: nowrap;
  }

  .name-mark__first { left: 158px; top: 82px; }
  .name-mark__last  { left: 100px; top: 150px; }

  .tagline {
    position: absolute;
    left: 214px;
    top: 232px;
    font-family: var(--body-font);
    font-size: 15px;
    letter-spacing: 2px;
    color: var(--ink);
    white-space: nowrap;
  }

  .tagline__role { color: var(--magenta); }
  .tagline__dot  { color: var(--ink); }

  /* Back */
  .card--back {
    left: 625px;
    background: var(--magenta);
    color: var(--paper);
  }

  .initials-badge {
    position: absolute;
    left: 220px;
    top: 106px;
    width: 76px;
    height: 76px;
    border-radius: 50%;
    background: var(--paper);
    display: flex;
    align-items: center;
    justify-content: center;
    font-family: var(--body-font);
    font-size: 30px;
    color: var(--magenta);
    letter-spacing: 1px;
  }

  .contact {
    position: absolute;
    left: 0;
    width: 100%;
    top: 232px;
    text-align: center;
    font-family: var(--body-font);
  }

  .contact__email {
    display: block;
    font-size: 15px;
    letter-spacing: 1.6px;
  }

  .contact__phone {
    display: block;
    margin-top: 6px;
    font-size: 19px;
    letter-spacing: 1.5px;
  }
</style>
</head>
<body>
  <main class="sheet">
    <section class="card card--front" aria-label="Card front">
      <div class="flourish-area" role="img" aria-label="Pink swirling flourishes and distressed texture surrounding the name"></div>
      <h1 class="name-mark">
        <span class="name-mark__first">Rosalind</span>
        <span class="name-mark__last">Pember</span>
      </h1>
      <p class="tagline">ROSALIND PEMBER <span class="tagline__dot">•</span><span class="tagline__role">STYLIST</span><span class="tagline__dot">•</span></p>
    </section>

    <section class="card card--back" aria-label="Card back">
      <div class="initials-badge">RP</div>
      <address class="contact">
        <span class="contact__email">rosapember@quillnet.co.nz</span>
        <span class="contact__phone">0218846193</span>
      </address>
    </section>
  </main>
</body>
</html>
```